Our private family owned investment company owns a vineyard in Napa. We want to design a label to put on our wine bottles once wine is ready. We would like artists to develop a creative design for a new label using this wording: Vineyard 48217. The dimensions of the label will be the standard label size on a 750 ml wine bottle. We appreciate creative flair, a classy look, preferably color but open to black and white too; maybe submit both ways. **As more explanation for designers, our family founded and owned a business for over 50 years and our logo was a teal colored snowflake (see attached jpeg logo). Our first plant address was numbered 48217. After our business was sold, our new family office is on located at 48217 Holloway. We have created a new business logo (see attached blue TRV logo) So the 48217 and 2 logos all have lineage and sentimental value to our family. Thank you for providing your unique creativity to this project.

Target Market(s)

to inspire conversation and reminiscing among friends and business associates when entertaining them.

Industry/Entity Type

Investment

Colors

Designer to choose colors to be used in the design.

Requirements
Must have
• Must Incorporate the wording: Vineyard 48217 - as part of the entire design and please see the attached logos (sketch of Vineyard 48217, blue snowflake logo, and TRV logo) and use any of these as a base, or part of, your new design. ** See project description for more detail on the meaning behind these logos.**

```html
<!DOCTYPE html>
<html lang="en">
<head>
<meta charset="utf-8">
<title>Vineyard 48217 – Cabernet Label</title>
<link rel="stylesheet" href="https://fonts.googleapis.com/css2?family=Open+Sans:wght@400;600;700&family=EB+Garamond:wght@400&display=swap">
<style>
  :root {
    --page: #ffffff;
    --label-bg: #ffffff;
    --label-edge: #b9b9b9;
    --wine-red: #d02e40;
    --vintage-red: #d4203f;
    --gold: #c8a56a;
    --gold-deep: #a8303a;
    --blush: #f3d6d6;
    --ink-grey: #555555;
    --type-white: #ffffff;
  }
  * { margin: 0; padding: 0; box-sizing: border-box; }
  html, body { width: 1200px; height: 1000px; overflow: hidden; background: var(--page); }
  .canvas { position: relative; width: 1200px; height: 1000px; }

  .label {
    position: absolute;
    left: 405px;
    width: 428px;
    height: 348px;
    background: var(--label-bg);
    border: 1px solid var(--label-edge);
    font-family: "Open Sans", sans-serif;
  }
  .label--front { top: 144px; }
  .label--back { top: 508px; }

  .rule-gold {
    position: absolute; left: 0; right: 0; height: 4px;
    background: linear-gradient(90deg, var(--gold) 0%, var(--gold) 30%, var(--gold-deep) 50%, var(--gold) 70%, var(--gold) 100%);
  }
  .rule-blush {
    position: absolute; left: 0; right: 0; height: 9px;
    background: linear-gradient(90deg, #fbeeee 0%, var(--blush) 30%, #c04a55 50%, var(--blush) 70%, #fbeeee 100%);
  }
  .rule-gold--top { top: 68px; }
  .rule-blush--top { top: 72px; }
  .rule-blush--bottom { top: 218px; }
  .rule-gold--bottom { top: 227px; }

  .band {
    position: absolute; left: 0; right: 0; top: 81px; height: 137px;
    background: var(--wine-red);
    color: var(--type-white);
  }
  .brand-name {
    position: absolute; left: 64px; top: 50px;
    font-size: 19px; font-weight: 400; letter-spacing: 0.5px;
    color: var(--type-white);
    line-height: 1;
    white-space: nowrap;
  }
  .info { position: absolute; left: 321px; top: 17px; width: 100px; }
  .info-title {
    font-size: 10px; font-weight: 700; letter-spacing: 2px; line-height: 1.2;
  }
  .info-text { font-size: 7px; line-height: 11px; margin-top: 2px; letter-spacing: 0.3px; }
  .info-title--address { margin-top: 14px; }

  .varietal {
    position: absolute; left: 46px; top: 244px;
    display: flex; align-items: center; gap: 6px;
  }
  .varietal-ornament {
    width: 30px; height: 24px; border-radius: 4px;
    background: linear-gradient(135deg, #e7b7bb, #b92f3f);
  }
  .varietal-name {
    font-family: "EB Garamond", serif;
    font-size: 16px; letter-spacing: 0.5px; color: var(--ink-grey);
  }
  .vintage {
    position: absolute; left: 107px; top: 313px;
    font-size: 14px; color: var(--vintage-red);
  }
  .measure {
    position: absolute; top: 327px;
    font-size: 9px; color: var(--ink-grey);
  }
  .measure--abv { left: 304px; }
  .measure--volume { left: 384px; }
</style>
</head>
<body>
<main class="canvas">

  <section class="label label--front">
    <div class="rule-gold rule-gold--top"></div>
    <div class="rule-blush rule-blush--top"></div>
    <div class="band">
      <p class="brand-name">VINEYARD 48217</p>
      <div class="info">
        <p class="info-title">CABERNET</p>
        <p class="info-text">Cabernet .xxxxxxx<br>xxxxxxxxxxxxxxxx<br>xxxxxxxxxxx</p>
        <p class="info-title info-title--address">ADDRESS</p>
        <p class="info-text">Vineyard 48217<br>48217 Holloway<br>Napa, CA</p>
      </div>
    </div>
    <div class="rule-blush rule-blush--bottom"></div>
    <div class="rule-gold rule-gold--bottom"></div>
    <div class="varietal">
      <div class="varietal-ornament" role="img" aria-label="Grape cluster and leaf ornament"></div>
      <span class="varietal-name">CABERNET</span>
      <div class="varietal-ornament" role="img" aria-label="Grape cluster and leaf ornament"></div>
    </div>
    <p class="vintage">2017</p>
    <p class="measure measure--abv">12% vol.</p>
    <p class="measure measure--volume">750 ml</p>
  </section>

  <section class="label label--back">
    <div class="rule-gold rule-gold--top"></div>
    <div class="rule-blush rule-blush--top"></div>
    <div class="band">
      <p class="brand-name">VINEYARD 48217</p>
      <div class="info">
        <p class="info-title">CABERNET</p>
        <p class="info-text">Cabernet .xxxxxxx<br>xxxxxxxxxxxxxxxx<br>xxxxxxxxxxx</p>
        <p class="info-title info-title--address">ADDRESS</p>
        <p class="info-text">Vineyard 48217<br>48217 Holloway<br>Napa, CA</p>
      </div>
    </div>
    <div class="rule-blush rule-blush--bottom"></div>
    <div class="rule-gold rule-gold--bottom"></div>
    <div class="varietal">
      <div class="varietal-ornament" role="img" aria-label="Grape cluster and leaf ornament"></div>
      <span class="varietal-name">CABERNET</span>
      <div class="varietal-ornament" role="img" aria-label="Grape cluster and leaf ornament"></div>
    </div>
    <p class="vintage">2017</p>
    <p class="measure measure--abv">12% vol.</p>
    <p class="measure measure--volume">750 ml</p>
  </section>

</main>
</body>
</html>
```